lifestyle photographer promotion piece

I would like to create a printed postcard to send to potential clients to introduce them to my work and hopefully create new clients. I'm a commercial photographer who just relocated to the Miami area and would really like to be getting more luxury lifestyle and resort work that includes my unique ability to shoot every aspect of lifestyle including food, travel, lifestyle and fashion. I'd like to incorporate between 4-12 of my best images from my online portfolio at www.lunadekkerfoto.com. The printed piece should also have a very clean, graphic, modern feel to it overall similar to my website. The main goal is to create a striking and compelling grouping of images showing my diverse offerings but in a way that shows an obvious visual style, my style. Please refer to my website for images. When winner is chosen, I will supply hi-res files to compete the design.
Updates

The card is a mailer and a handout. The back of the card should be black and white and text only with my info and an area for address to information. Dimensions of the card are 6x8.5 inches and I prefer the horizontal aspect ratio.

I've noticed a few designers are incorporating graphics. I would like to avoid that. Interested in photography dominated card with /or without graphic use of white space. I tend to avoid color backgrounds, white space is my preference in most cases although I'm not completely against it. 

Target Market(s)

Advertising Agencies and Magazines, Record Labels, Modeling Agencies, Public Relations Firms

Industry/Entity Type

Fashion

Requirements
Must have
• Horizontal

Front(color):
Marisol Tate Photography
Miami / Naples / New York

Back(black and white):
(239)614-2938
www.lunadekkerfoto.com
info@lunadekkerfoto.com

```html
<!DOCTYPE html>
<html lang="en">
<head>
<meta charset="utf-8">
<title>Marisol Tate Photography — Postcard Back</title>
<link rel="stylesheet" href="https://fonts.googleapis.com/css2?family=Cinzel:wght@400;700&display=swap">
<style>
  :root {
    --paper: #ffffff;
    --ink: #000000;
    --frame: #000000;
  }
  * { margin: 0; padding: 0; box-sizing: border-box; }
  html, body {
    width: 1200px;
    height: 852px;
    overflow: hidden;
    background: var(--paper);
  }
  .postcard-back {
    position: relative;
    width: 1200px;
    height: 852px;
    background: var(--paper);
    border: 1px solid var(--frame);
    color: var(--ink);
    font-family: "Cinzel", "Trajan Pro", serif;
  }
  .studio-name {
    position: absolute;
    left: 69px;
    top: 628px;
    font-size: 29px;
    font-weight: 400;
    letter-spacing: 1.2px;
    white-space: nowrap;
    line-height: 1;
  }
  .contact {
    position: absolute;
    left: 92px;
    top: 697px;
    list-style: none;
    font-size: 21px;
    line-height: 33px;
    letter-spacing: 0.6px;
    white-space: nowrap;
  }
  .contact-label {
    font-weight: 700;
    letter-spacing: 1px;
    margin-right: 4px;
  }
  .contact-value { font-weight: 400; }
  .contact-web {
    font-size: 15px;
    letter-spacing: 9.2px;
    line-height: 30px;
  }
</style>
</head>
<body>
  <main class="postcard-back">
    <h1 class="studio-name">Marisol Tate Photography</h1>
    <ul class="contact">
      <li class="contact-phone"><span class="contact-label">PHONE</span><span class="contact-value">(239)614-2938</span></li>
      <li class="contact-email"><span class="contact-label">EMAIL</span><span class="contact-value">info@lunadekkerfoto.com</span></li>
      <li class="contact-web">www.lunadekkerfoto.com</li>
    </ul>
  </main>
</body>
</html>
```